Natural and organic skincare brand needs label design!

I need labels designed for my natural and organic skincare brand lumavale. The front of the bottles must contain the logo (image attached) and the following words: Formulated by a Naturopath; Anti-aging therapy; Organic Facial Oil; with CoEnzyme Q10 and Rosehip Seed Oil; 100ml e3.38fl.oz. Colours I would like used include black/white/grey/silver and aqua. I also like the grey woodgrain used on my draft website (check out www.lumavale-skin.com.au). The logo should be silver foil (shiny).The final design should be simple and communicate nature and sophistication. Some designs I like are found in the attachments. I intend to use black or white bottles.

Target Market(s)

women aged 30-50 interested in natural products

Industry/Entity Type

Skin Care Product

Font styles to use
Serif
Sans Serif
Decorative
Script
Other font styles liked:
• Any

Requirements
Must have
• Dimensions: 62mm (w) x 75mm (H) (front label only)
• Must contain the logo (image attached). The logo should be silver foil (shiny). and the following words are to be included on the label:
• Formulated by a Naturopath;
• Anti-aging Therapy;
• Organic Facial Oil;
• with CoEnzyme Q10 and Rosehip Seed Oil;
• 100ml e3.38fl.oz.
Nice to have
• Colours I would like used include black/white/grey/silver and aqua (turquoise). But I am also open to suggestion. I also like the grey woodgrain used on my draft website (check out www.lumavale-skin.com.au)

```html
<!DOCTYPE html>
<html lang="en">
<head>
<meta charset="utf-8">
<title>lumavale – Anti-Aging Therapy front label</title>
<link rel="stylesheet" href="https://fonts.googleapis.com/css2?family=Raleway:wght@300;400;500&display=swap">
<style>
  :root {
    --canvas-bg: #efefef;
    --wood-light: #f1f0ee;
    --wood-mid: #dcdbd8;
    --wood-dark: #c9c8c5;
    --panel: #f7f7f7;
    --aqua: #2fc6cc;
    --slate: #3c4654;
    --ink: #5a6270;
  }
  html, body {
    margin: 0;
    padding: 0;
    width: 1200px;
    height: 1030px;
    overflow: hidden;
    background: var(--canvas-bg);
    font-family: "Raleway", sans-serif;
  }
  .label {
    position: absolute;
    left: 212px;
    top: 45px;
    width: 776px;
    height: 940px;
    box-shadow: 0 2px 14px rgba(0,0,0,0.08);
  }
  .label__woodgrain {
    position: absolute;
    inset: 0;
    background: linear-gradient(180deg, var(--wood-light) 0%, var(--wood-mid) 45%, var(--wood-light) 70%, var(--wood-dark) 100%);
  }
  .label__panel {
    position: absolute;
    left: 58px;
    right: 58px;
    top: 190px;
    bottom: 70px;
    background: var(--panel);
    border: 5px solid var(--aqua);
    box-sizing: border-box;
    text-align: center;
    color: var(--slate);
  }
  .brand {
    position: absolute;
    left: 50%;
    top: -42px;
    transform: translateX(-50%);
    display: flex;
    align-items: center;
    gap: 16px;
    padding: 14px 26px;
    background: var(--panel);
    border-radius: 40px;
  }
  .brand__dot {
    width: 44px;
    height: 44px;
    border-radius: 50%;
    background: var(--slate);
  }
  .brand__name {
    font-weight: 400;
    font-size: 38px;
    letter-spacing: 2px;
    color: var(--slate);
  }
  .title__line1 {
    margin: 120px 0 0;
    font-weight: 300;
    font-size: 84px;
    line-height: 1;
    letter-spacing: 1px;
  }
  .title__line2 {
    margin: 4px 0 0;
    font-weight: 300;
    font-size: 112px;
    line-height: 1;
  }
  .subtitle {
    margin: 6px 0 0;
    font-weight: 500;
    font-size: 38px;
    letter-spacing: 4px;
    color: var(--aqua);
  }
  .rule {
    width: 360px;
    height: 2px;
    margin: 16px auto 0;
    background: var(--aqua);
  }
  .ingredients {
    margin: 18px 0 0;
    font-size: 19px;
    color: var(--ink);
  }
  .claim {
    margin: 100px 0 0;
    font-size: 30px;
    color: var(--ink);
  }
  .volume {
    margin: 16px 0 0;
    font-size: 22px;
    color: var(--ink);
  }
</style>
</head>
<body>
  <main class="label">
    <div class="label__woodgrain" role="img" aria-label="Grey whitewashed woodgrain texture background"></div>
    <section class="label__panel">
      <div class="brand">
        <span class="brand__dot"></span>
        <span class="brand__name">lumavale</span>
      </div>
      <h1 class="title__line1">ANTI-AGING</h1>
      <h2 class="title__line2">THERAPY</h2>
      <p class="subtitle">ORGANIC FACIAL OIL</p>
      <div class="rule"></div>
      <p class="ingredients">with CoEnzyme Q10 and Rosehip Seed Oil</p>
      <p class="claim">Formulated by a Naturopath</p>
      <div class="rule"></div>
      <p class="volume">100ml&nbsp; e3.38fl.oz</p>
    </section>
  </main>
</body>
</html>
```